KVT Building And Maintenance

Need a very professional looking double sided Buisiness card with all my details phone number, name, email, license number.

Target Market(s)

construction industry

Industry/Entity Type

building

Contact Information for Business Card

Name Dale Pemberton. Email Address Info@KVTBuilding.com.au mobile number 0452918736 licence number 671093D. web site

```html
<!DOCTYPE html>
<html lang="en">
<head>
<meta charset="utf-8">
<title>KVT Building And Maintenance – Business Card</title>
<link href="https://fonts.googleapis.com/css2?family=Montserrat:wght@400;500;600;700&display=swap" rel="stylesheet">
<style>
  :root {
    --backdrop: #3a3a3a;
    --card-white: #ffffff;
    --card-black: #141414;
    --brand-blue: #2a9ad8;
    --ink-dark: #3b3b3b;
    --ink-mid: #5a5a5a;
    --ink-light: #ffffff;
  }
  * { box-sizing: border-box; margin: 0; padding: 0; }
  html, body {
    width: 1200px; height: 801px; overflow: hidden;
    background: var(--backdrop);
    font-family: "Montserrat", Arial, sans-serif;
  }
  .sheet {
    width: 1200px; height: 801px;
    display: flex; align-items: center; justify-content: center; gap: 40px;
  }
  .card {
    width: 540px; height: 310px; position: relative;
    border-bottom: 3px solid var(--brand-blue);
  }
  .card--front { background: var(--card-white); }
  .card--back {
    background: var(--card-black);
    display: flex; align-items: center; justify-content: center;
    border: 2px solid var(--brand-blue);
  }
  .wordmark {
    position: absolute; left: 150px; top: 70px;
    display: flex; align-items: center; gap: 12px;
    font-weight: 700; font-size: 40px; letter-spacing: 2px;
    color: var(--ink-dark); text-transform: uppercase;
  }
  .wordmark__square { width: 22px; height: 22px; background: var(--ink-dark); }
  .holder {
    position: absolute; left: 60px; top: 190px; width: 200px;
  }
  .holder__name {
    font-weight: 700; font-size: 17px; color: var(--brand-blue);
    text-transform: uppercase; letter-spacing: 0.5px;
  }
  .holder__licence { font-size: 13px; color: var(--ink-mid); margin-top: 4px; }
  .divider {
    position: absolute; left: 275px; top: 178px;
    width: 1px; height: 62px; background: var(--brand-blue);
  }
  .contacts {
    position: absolute; left: 295px; top: 180px;
    list-style: none; font-size: 13px; color: var(--ink-mid);
  }
  .contacts li { display: flex; align-items: center; gap: 8px; height: 20px; }
  .contacts svg { width: 12px; height: 12px; fill: var(--brand-blue); flex: none; }
  .back-mark {
    color: var(--ink-light); font-weight: 700; font-size: 54px;
    letter-spacing: 3px; text-transform: uppercase; text-align: center; line-height: 1.05;
  }
  .back-mark span { display: block; font-size: 40px; }
</style>
</head>
<body>
<main class="sheet">
  <section class="card card--front" aria-label="Business card front">
    <div class="wordmark"><span class="wordmark__square"></span>KVT Building</div>
    <div class="holder">
      <p class="holder__name">Dale Pemberton</p>
      <p class="holder__licence">licence number 671093D</p>
    </div>
    <div class="divider"></div>
    <ul class="contacts">
      <li><svg viewBox="0 0 24 24"><path d="M6.6 10.8a15 15 0 0 0 6.6 6.6l2.2-2.2a1 1 0 0 1 1-.25 11.4 11.4 0 0 0 3.6.57 1 1 0 0 1 1 1V20a1 1 0 0 1-1 1A17 17 0 0 1 3 4a1 1 0 0 1 1-1h3.5a1 1 0 0 1 1 1c0 1.25.2 2.45.57 3.57a1 1 0 0 1-.25 1z"/></svg>0452918736</li>
      <li><svg viewBox="0 0 24 24"><path d="M2 5h20v14H2z M2 5l10 8 10-8" /></svg>Info@KVTBuilding.com.au</li>
      <li><svg viewBox="0 0 24 24"><circle cx="12" cy="12" r="10"/></svg>www.KVTBuilding.com.au</li>
    </ul>
  </section>
  <section class="card card--back" aria-label="Business card back">
    <p class="back-mark">KVT<span>Building</span></p>
  </section>
</main>
</body>
</html>
```